Business Card Design Project

I need a new business card design for my Remodel/Design/Build company, Brightfield Renovation Works, Inc. See our website: www.brightfieldrenovationworks.com
We are an established company with a growing reputation and growing quickly. We are know for being on the forward edge of the industry, producing a great product and our "people friendly" approach.
I am looking for something cool, transitional, maybe even retro that captures the imagination, shows our sleek creativity and streamlined approach as well as communicates stability and trustworthiness.
Updates

Stainless steel business card design would be cool.

Please have all future designs with full logo colors and shown on a stainless steel business card.  Also, logo and tag line will most likely be printed with spot uv, so layers will be necessary.  Thank you.

Target Market(s)

30-65 yrs old, homeowners, appreciate fine things, median income $150+k, net worth $1+m

Industry/Entity Type

Business

Requirements
Must have
• Company Logo
Contact information
Website URL
Nice to have
• Tagline: Building Relationships and Remodeling Homes...One Client at a Time.
Double-sided okay.
Stainless steel business card.

```html
<!DOCTYPE html>
<html lang="en">
<head>
<meta charset="utf-8">
<title>Brightfield Renovation Works – Business Card</title>
<link href="https://fonts.googleapis.com/css2?family=Nunito+Sans:ital,wght@0,400;0,600;0,700;1,400;1,600&display=swap" rel="stylesheet">
<style>
  :root {
    --backdrop: #d9d7d7;
    --steel-light: #8e8e8e;
    --steel-mid: #767676;
    --steel-dark: #5a5a5a;
    --ink: #3b3b3b;
    --ink-soft: #454545;
    --tagline: #ececec;
    --brand-red: #9c2126;
  }
  * { margin: 0; padding: 0; box-sizing: border-box; }
  html, body {
    width: 1200px; height: 900px; overflow: hidden;
    background: var(--backdrop);
    font-family: "Nunito Sans", Arial, sans-serif;
  }
  .card {
    position: absolute; left: 271px; width: 679px; height: 383px;
    background: linear-gradient(180deg, var(--steel-light) 0%, var(--steel-mid) 55%, var(--steel-dark) 100%);
    overflow: hidden;
  }
  .card--front { top: 50px; }
  .card--back { top: 466px; }

  .brand { position: absolute; display: flex; align-items: center; gap: 12px; }
  .brand__dot { width: 66px; height: 66px; border-radius: 50%; background: var(--brand-red); flex: none; }
  .brand__name { color: var(--brand-red); font-weight: 700; line-height: 1; }
  .brand__line1 { display: block; font-size: 37px; letter-spacing: 1.5px; }
  .brand__line2 { display: block; font-size: 16px; letter-spacing: 5px; margin-top: 5px; }
  .card--front .brand { left: 42px; top: 48px; }
  .card--back .brand { left: 150px; top: 128px; }

  .contact { position: absolute; right: 50px; top: 164px; text-align: right; color: var(--ink); }
  .contact__name { font-size: 26px; font-weight: 700; line-height: 1.2; }
  .contact__title { font-size: 19px; font-style: italic; line-height: 1.2; color: var(--ink-soft); }
  .contact__lines { margin-top: 27px; font-size: 20px; line-height: 25px; }
  .contact__label { font-weight: 700; }

  .tagline { position: absolute; color: var(--tagline); font-style: italic; font-size: 16px; white-space: nowrap; }
  .card--front .tagline { right: 47px; top: 339px; }
  .card--back .tagline { left: 0; right: 0; top: 32px; text-align: center; }

  .web { position: absolute; left: 0; right: 0; top: 338px; text-align: center; font-size: 20px; color: var(--ink); }
</style>
</head>
<body>
  <section class="card card--front">
    <div class="brand">
      <span class="brand__dot"></span>
      <span class="brand__name">
        <span class="brand__line1">BRIGHTFIELD</span>
        <span class="brand__line2">RENOVATION WORKS</span>
      </span>
    </div>
    <div class="contact">
      <p class="contact__name">Dana Whitlock</p>
      <p class="contact__title">President</p>
      <div class="contact__lines">
        <p><span class="contact__label">Phone.</span> 555-214-3370&nbsp; <span class="contact__label">Fax.</span> 555-214-3378</p>
        <p><span class="contact__label">Email.</span> danawhitlock@brightfieldrenovationworks.com</p>
        <p>www.brightfieldrenovationworks.com</p>
      </div>
    </div>
    <p class="tagline">Earning Lasting Trust and Transforming Houses… One Family at a Time.</p>
  </section>

  <section class="card card--back">
    <p class="tagline">Earning Lasting Trust and Transforming Houses… One Family at a Time.</p>
    <div class="brand">
      <span class="brand__dot"></span>
      <span class="brand__name">
        <span class="brand__line1">BRIGHTFIELD</span>
        <span class="brand__line2">RENOVATION WORKS</span>
      </span>
    </div>
    <p class="web">www.brightfieldrenovationworks.com</p>
  </section>
</body>
</html>
```